CoinLantern one-page corporate website

Our company, CoinLantern is a cryptocurrency Initial Coin Offering ("ICO" marketing and promotion agency, which requires a professional company landing page design whereby prospective clients can learn;
-who we are
-what we do
-what our people are saying about us
-core team members
-subscribe to our mailing list
-how to get in touch (basic contact form)

We are looking for something unique and attractive -- not a standard Pako template that we could put together ourselves. Plain stock images should not be used. Unique visualizations of the service offerings and creative presentation are key. We are a cutting edge marketing agency and as such, we need to look the part.

Relevant documentation about the business and branding assets have been attached to guide the designer. Certain information will be included by the company at a later date such as team member descriptions. As such, lorem ipsum may be included wherever necessary to help visualize the textual areas.

****Please ensure that you actually utilize the photos and graphics provided so that we can have a good picture of what it would actually look like with our branding.

The site must be responsive HTML CSS Design.

Sites style themes we like for inspiration and specific sections we like ****Very important***:
https://vaultorbitra.example/offers - we like that the token & company logo is used in unique visualizations that connects various ideas together. We imagine unique visuals such as these with our Icon (see attached) serving as a token. We also like the unique and attractive visual theme of the webpage itself.

https://quarrelstone.example/ - we like the layout of this website, specifically how the service offerings are displayed in a circular visual graphic with the Quarrel logo in the middle. We imagine a similar type of graphic designed with CoinLantern in the middle.

https://zorvinet.example/ - we like how the logo is central to the theme in this site when you first enter and how it fades + shrinks into the distance as you scroll down.

Target Market(s)

cryptocurrency entrepreneurs and ICOs

Industry/Entity Type

It Company

Coding

Coded - Design and coding required

Number of Pages Required

1 page

Font styles to use
Sans Serif

Colors

Designer to choose colors to be used in the design.

Requirements
Must have
• The site must be responsive HTML CSS Design.
• The page must be modern and visually attractive. Elements must not be static and should have a fluid motion / visual change as the user scrolls through the page.
Should not have
• The project should not use any old stock images or elements which are dull and over-used, but rather images or elements should be unique and well thought out.

```html
<!DOCTYPE html>
<html lang="en">
<head>
<meta charset="utf-8">
<title>CoinLantern — ICO Marketing Agency</title>
<link href="https://fonts.googleapis.com/css2?family=Montserrat:wght@300;400;600;700&family=Open+Sans:wght@400;600&display=swap" rel="stylesheet">
<style>
:root{
  --hero-top:#20243a;
  --hero-mid:#3a3960;
  --hero-violet:#4b4674;
  --ridge-light:#8c8c96;
  --ridge-dark:#3c3c46;
  --navy:#131938;
  --navy-icon:#1f2648;
  --ring-blue:#1d64b0;
  --ring-bright:#2b8fe0;
  --contact-top:#5a4a86;
  --contact-low:#4a3f74;
  --team-bg:#463c6a;
  --card:rgba(255,255,255,0.12);
  --card-hi:rgba(255,255,255,0.22);
  --field:rgba(255,255,255,0.12);
  --accent:#1c4a7e;
  --link-blue:#2b7fc8;
  --strip:#26262c;
  --footer:#2a2a30;
  --bottom:#222227;
  --white:#ffffff;
  --glyph:#4a4560;
  --soft:#c9c9d6;
  --muted:#8d8d99;
}
*{margin:0;padding:0;box-sizing:border-box}
html,body{width:1200px;height:3273px;overflow:hidden}
body{position:relative;font-family:'Open Sans',Arial,sans-serif;color:var(--white);background:var(--bottom)}
.abs{position:absolute}

/* hero */
.hero{left:0;top:0;width:1200px;height:524px;
  background:
    radial-gradient(ellipse 520px 160px at 300px 470px,rgba(160,160,170,.55),transparent 70%),
    radial-gradient(ellipse 600px 170px at 950px 460px,rgba(150,150,162,.5),transparent 70%),
    radial-gradient(ellipse 700px 260px at 600px 240px,rgba(90,80,140,.45),transparent 75%),
    linear-gradient(180deg,var(--hero-top) 0%,var(--hero-mid) 48%,var(--hero-violet) 70%,var(--ridge-light) 84%,var(--ridge-dark) 100%)}
.nav a{position:absolute;top:36px;font-family:'Montserrat',Arial,sans-serif;font-weight:700;font-size:15px;color:var(--white);text-decoration:none;letter-spacing:.3px}
.brand{position:absolute;left:473px;top:24px;display:flex;align-items:center;gap:10px;font-family:'Montserrat',Arial,sans-serif;font-weight:400;font-size:28px;color:var(--white)}
.brand-dot{width:40px;height:40px;border:2px solid var(--white);border-radius:50%}
.search{position:absolute;left:1144px;top:36px}
.hero-copy{position:absolute;left:130px;top:176px;width:940px;text-align:center;font-family:'Montserrat',Arial,sans-serif;font-weight:300;font-size:29px;line-height:39px}
.hero-copy b{font-weight:700}
.btn-start{position:absolute;left:478px;top:360px;width:262px;height:50px;border:2px solid var(--white);border-radius:25px;text-align:center;line-height:46px;font-family:'Montserrat',Arial,sans-serif;font-weight:600;font-size:21px}
.chevron{position:absolute;left:586px;top:494px}

/* what we do */
.services{left:0;top:524px;width:1200px;height:818px;background:radial-gradient(circle 420px at 600px 469px,#172050,var(--navy) 80%)}
.section-title{position:absolute;left:0;width:1200px;text-align:center;font-family:'Montserrat',Arial,sans-serif;font-weight:300;letter-spacing:2px}
.svc-icon{position:absolute;width:88px;height:88px;border-radius:50%;background:var(--navy-icon);display:flex;align-items:center;justify-content:center}
.svc-text{position:absolute;font-size:15px;line-height:19px;color:var(--soft)}
.svc-text.left{text-align:right}

/* contact */
.contact{left:0;top:1342px;width:1200px;height:465px;background:
  radial-gradient(ellipse 500px 200px at 700px 120px,rgba(120,100,180,.35),transparent 70%),
  linear-gradient(180deg,var(--contact-top),var(--contact-low))}
.field{position:absolute;background:var(--field);font-size:12px;color:var(--soft);padding:8px 14px}
.field svg{position:absolute;right:12px;top:11px}
.btn-submit{position:absolute;left:620px;top:1728px;width:303px;height:42px;background:var(--accent);text-align:center;line-height:42px;font-family:'Montserrat',Arial,sans-serif;font-weight:700;font-size:15px}

/* team */
.team{left:0;top:1807px;width:1200px;height:724px;background:var(--team-bg)}
.card{position:absolute;top:1963px;width:322px;height:546px;background:var(--card);text-align:center}
.card.featured{background:var(--card-hi)}
.portrait{position:absolute;left:56px;top:44px;width:210px;height:210px;border-radius:50%;border:6px solid var(--white)}
.member-name{position:absolute;left:0;top:306px;width:100%;font-family:'Montserrat',Arial,sans-serif;font-weight:700;font-size:23px}
.member-role{position:absolute;left:0;top:340px;width:100%;font-size:12px;color:var(--soft)}
.member-phone{position:absolute;left:0;top:384px;width:100%;font-family:'Montserrat',Arial,sans-serif;font-weight:700;font-size:16px}
.member-mail{position:absolute;left:0;top:418px;width:100%;font-size:12px;color:var(--soft)}
.socials{position:absolute;left:0;top:472px;width:100%;display:flex;justify-content:center;gap:18px}
.socials span{width:28px;height:28px;border-radius:50%;background:rgba(255,255,255,0.88);display:flex;align-items:center;justify-content:center}
.socials span.active{background:var(--link-blue)}
.to-top{position:absolute;width:44px;height:44px;background:#2a2a33;display:flex;align-items:center;justify-content:center}

/* info strip */
.info{left:0;top:2531px;width:1200px;height:273px;background:radial-gradient(ellipse 500px 140px at 700px 60px,#2e2e36,var(--strip) 80%)}
.info-item{position:absolute;top:2592px;width:240px;text-align:center}
.info-icon{width:44px;height:44px;margin:0 auto;background:var(--accent);display:flex;align-items:center;justify-content:center}
.info-label{margin-top:14px;font-size:16px;letter-spacing:1px;color:var(--muted)}
.hours{margin-top:10px;font-size:12px;line-height:22px;color:var(--soft)}

/* footer */
.footer{left:0;top:2804px;width:1200px;height:377px;background:var(--footer)}
.foot-brand{position:absolute;left:94px;top:2896px;width:345px;text-align:center}
.foot-brand .ring{width:88px;height:88px;margin:0 auto;border:3px solid var(--white);border-radius:50%}
.foot-brand .name{margin-top:14px;font-family:'Montserrat',Arial,sans-serif;font-weight:400;font-size:46px;letter-spacing:1px}
.foot-title{position:absolute;top:2864px;font-family:'Montserrat',Arial,sans-serif;font-weight:700;font-size:15px;letter-spacing:.5px}
.client{position:absolute;width:48px;height:48px;border-radius:50%;border:2px solid var(--muted);opacity:.7}
.news-copy{position:absolute;left:888px;top:2928px;width:230px;font-size:12px;line-height:21px;color:var(--soft)}
.news-input{position:absolute;left:888px;top:3028px;width:233px;height:38px;background:#35353d;font-size:12px;color:var(--muted);padding:10px 14px}
.news-go{position:absolute;right:0;top:0;width:40px;height:38px;background:var(--accent);display:flex;align-items:center;justify-content:center}

.bottom{left:0;top:3181px;width:1200px;height:92px;background:var(--bottom)}
.bottom-socials{position:absolute;left:970px;top:3217px;display:flex;gap:7px}
.bottom-socials svg{display:block}
</style>
</head>
<body>

<header class="abs hero" role="img" aria-label="Starry night sky over a grey mountain range"></header>
<nav class="nav">
  <a style="left:83px">HOME</a>
  <a style="left:175px">ABOUT US</a>
  <a style="left:290px">SERVICES</a>
  <a style="left:785px">CORE TEAM</a>
  <a style="left:912px">CONTACT US</a>
  <a style="left:1049px">FAQ</a>
</nav>
<div class="brand"><span class="brand-dot"></span>CoinLantern</div>
<svg class="search" width="16" height="16" viewBox="0 0 16 16"><circle cx="6.5" cy="6.5" r="5" fill="none" stroke="#fff" stroke-width="2"/><line x1="10" y1="10" x2="15" y2="15" stroke="#fff" stroke-width="2"/></svg>
<p class="hero-copy"><b>CoinLantern</b> is the premier marketing agency for ICO's. Our experts will ensure that your <b>ICO</b> is run properly, communicated well, and achieves your desired outcomes</p>
<div class="btn-start">GET STARTED</div>
<svg class="chevron" width="28" height="14" viewBox="0 0 28 14"><polyline points="2,2 14,12 26,2" fill="none" stroke="#fff" stroke-width="2"/></svg>

<section class="abs services">
  <h2 class="section-title" style="top:92px;font-size:44px">WHAT WE DO</h2>
  <svg class="abs" style="left:0;top:0" width="1200" height="818" viewBox="0 0 1200 818">
    <circle cx="600" cy="469" r="330" fill="none" stroke="#1b2246" stroke-width="1"/>
    <circle cx="600" cy="469" r="250" fill="none" stroke="#1b2246" stroke-width="1"/>
    <circle cx="600" cy="469" r="118" fill="#152048"/>
    <circle cx="600" cy="469" r="128" fill="none" stroke="var(--ring-blue)" stroke-width="10" stroke-dasharray="560 244" transform="rotate(-60 600 469)"/>
    <circle cx="600" cy="469" r="146" fill="none" stroke="var(--ring-blue)" stroke-width="8" stroke-dasharray="250 668" transform="rotate(-20 600 469)"/>
    <circle cx="600" cy="469" r="96" fill="none" stroke="var(--ring-bright)" stroke-width="3" opacity=".6"/>
    <text x="600" y="477" text-anchor="middle" fill="#2b8fe0" font-family="Montserrat, Arial, sans-serif" font-weight="600" font-size="24">CoinLantern</text>
  </svg>
</section>

<p class="svc-text left" style="left:78px;top:776px;width:230px">Connections to the best legal and accounting practices depending on your situation</p>
<div class="svc-icon" style="left:351px;top:757px"><svg width="34" height="30" viewBox="0 0 34 30"><rect x="2" y="2" width="30" height="20" fill="none" stroke="#fff" stroke-width="2.4"/><line x1="10" y1="27" x2="24" y2="27" stroke="#fff" stroke-width="2.4"/><circle cx="17" cy="12" r="3" fill="#fff"/></svg></div>

<p class="svc-text left" style="left:44px;top:965px;width:200px">Token sale strategy</p>
<div class="svc-icon" style="left:288px;top:927px"><svg width="34" height="22" viewBox="0 0 34 22"><path d="M2 11 Q17 -6 32 11 Q17 28 2 11Z" fill="#fff"/><circle cx="17" cy="11" r="5" fill="var(--navy-icon)"/></svg></div>

<p class="svc-text left" style="left:60px;top:1169px;width:250px">Secure Token Launch Websitee</p>
<div class="svc-icon" style="left:351px;top:1112px"><svg width="32" height="20" viewBox="0 0 32 20"><polyline points="2,18 12,8 18,14 30,2" fill="none" stroke="#fff" stroke-width="2.6"/><polyline points="22,2 30,2 30,10" fill="none" stroke="#fff" stroke-width="2.6"/></svg></div>

<div class="svc-icon" style="left:765px;top:757px"><svg width="24" height="22" viewBox="0 0 24 22"><polyline points="3,3 11,11 3,19" fill="none" stroke="#fff" stroke-width="2.6"/><line x1="20" y1="3" x2="20" y2="19" stroke="#fff" stroke-width="2.6"/></svg></div>
<p class="svc-text" style="left:877px;top:776px;width:200px">Whitepaper Consultation and Review</p>

<div class="svc-icon" style="left:829px;top:927px"><svg width="30" height="24" viewBox="0 0 30 24"><g fill="#fff"><rect x="2" y="3" width="4" height="4"/><rect x="2" y="10" width="4" height="4"/><rect x="2" y="17" width="4" height="4"/><rect x="10" y="4" width="18" height="2.4"/><rect x="10" y="11" width="18" height="2.4"/><rect x="10" y="18" width="18" height="2.4"/></g></svg></div>
<p class="svc-text" style="left:936px;top:962px;width:200px">Raise amount and future token price strategy</p>

<div class="svc-icon" style="left:765px;top:1112px"><svg width="30" height="28" viewBox="0 0 30 28"><path d="M2 2h20v14H8l-6 6z" fill="#fff"/><path d="M24 8h4v18l-5-5H10v-3h14z" fill="#fff"/></svg></div>
<p class="svc-text" style="left:873px;top:1149px;width:230px">KYC (Know Your Customer) strategies</p>

<section class="abs contact" role="img" aria-label="Violet starry sky backdrop">
  <h2 class="section-title" style="top:120px;font-size:44px">CONTACT US</h2>
  <p class="section-title" style="top:186px;font-size:22px;letter-spacing:1px">INSERT YOUR CONTACT INFORMATION</p>
</section>
<div class="field" style="left:279px;top:1599px;width:304px;height:38px">Name*<svg width="16" height="16" viewBox="0 0 16 16"><circle cx="8" cy="5" r="3.2" fill="#fff"/><path d="M2 15c0-4 3-6 6-6s6 2 6 6z" fill="#fff"/></svg></div>
<div class="field" style="left:279px;top:1662px;width:304px;height:38px">Email*<svg width="16" height="14" viewBox="0 0 16 14"><rect x="1" y="2" width="14" height="10" fill="none" stroke="#fff" stroke-width="1.8"/><polyline points="1,2 8,8 15,2" fill="none" stroke="#fff" stroke-width="1.8"/></svg></div>
<div class="field" style="left:279px;top:1728px;width:304px;height:38px">Website*<svg width="16" height="16" viewBox="0 0 16 16"><circle cx="8" cy="8" r="6.5" fill="none" stroke="#fff" stroke-width="1.8"/><ellipse cx="8" cy="8" rx="2.8" ry="6.5" fill="none" stroke="#fff" stroke-width="1.4"/><line x1="1.5" y1="8" x2="14.5" y2="8" stroke="#fff" stroke-width="1.4"/></svg></div>
<div class="field" style="left:620px;top:1597px;width:303px;height:94px">Message*</div>
<div class="btn-submit">SUBMIT YOUR MESSAGE</div>

<svg width="0" height="0" style="position:absolute">
  <defs>
    <g id="ico-share"><circle cx="4" cy="8" r="2.2"/><circle cx="12" cy="3.5" r="2.2"/><circle cx="12" cy="12.5" r="2.2"/><path d="M4 8L12 3.5M4 8L12 12.5" stroke-width="1.5" fill="none"/></g>
    <g id="ico-chat"><path d="M2 3h12v8H7l-3 3v-3H2z"/></g>
    <g id="ico-globe"><circle cx="8" cy="8" r="6" fill="none" stroke-width="1.6"/><path d="M2 8h12M8 2v12" stroke-width="1.4" fill="none"/></g>
    <g id="ico-link"><rect x="1.5" y="5.5" width="7" height="5" rx="2.5" fill="none" stroke-width="1.6"/><rect x="7.5" y="5.5" width="7" height="5" rx="2.5" fill="none" stroke-width="1.6"/></g>
    <g id="ico-mail"><rect x="2" y="4" width="12" height="8" fill="none" stroke-width="1.6"/><path d="M2 4l6 5 6-5" fill="none" stroke-width="1.6"/></g>
    <g id="ico-star"><path d="M8 2l1.8 3.8 4.2.5-3.1 2.9.8 4.1L8 11.3 4.3 13.3l.8-4.1L2 6.3l4.2-.5z"/></g>
  </defs>
</svg>

<section class="abs team">
  <h2 class="section-title" style="top:44px;font-size:50px;letter-spacing:1px">CORE TEAM MEMBERS</h2>
</section>
<article class="card" style="left:81px">
  <div class="portrait" role="img" aria-label="Portrait photo of Dorian Vale" style="background:linear-gradient(180deg,#8fa6bd 0%,#b59680 45%,#3c4a5a 100%)"></div>
  <h3 class="member-name">DORIAN VALE</h3>
  <p class="member-role">Lead Designer</p>
  <p class="member-phone">+1 (555) 0148273</p>
  <p class="member-mail">✉ dorian@coinlantern.example</p>
  <div class="socials">
    <span><svg width="16" height="16" viewBox="0 0 16 16" fill="var(--glyph)" stroke="var(--glyph)"><use href="#ico-share"/></svg></span>
    <span><svg width="16" height="16" viewBox="0 0 16 16" fill="var(--glyph)" stroke="var(--glyph)"><use href="#ico-chat"/></svg></span>
    <span><svg width="16" height="16" viewBox="0 0 16 16" fill="var(--glyph)" stroke="var(--glyph)"><use href="#ico-globe"/></svg></span>
    <span><svg width="16" height="16" viewBox="0 0 16 16" fill="var(--glyph)" stroke="var(--glyph)"><use href="#ico-link"/></svg></span>
    <span><svg width="16" height="16" viewBox="0 0 16 16" fill="var(--glyph)" stroke="var(--glyph)"><use href="#ico-mail"/></svg></span>
    <span><svg width="16" height="16" viewBox="0 0 16 16" fill="var(--glyph)" stroke="var(--glyph)"><use href="#ico-star"/></svg></span>
  </div>
</article>
<article class="card featured" style="left:441px">
  <div class="portrait" role="img" aria-label="Portrait photo of Marek Olund" style="background:linear-gradient(180deg,#6a3a28 0%,#c08a6c 40%,#2a1a16 100%)"></div>
  <h3 class="member-name">MAREK OLUND</h3>
  <p class="member-role">Art Director</p>
  <p class="member-phone">+1 (555) 0148273</p>
  <p class="member-mail">✉ marek@coinlantern.example</p>
  <div class="socials">
    <span><svg width="16" height="16" viewBox="0 0 16 16" fill="var(--glyph)" stroke="var(--glyph)"><use href="#ico-share"/></svg></span>
    <span><svg width="16" height="16" viewBox="0 0 16 16" fill="var(--glyph)" stroke="var(--glyph)"><use href="#ico-chat"/></svg></span>
    <span><svg width="16" height="16" viewBox="0 0 16 16" fill="var(--glyph)" stroke="var(--glyph)"><use href="#ico-globe"/></svg></span>
    <span class="active"><svg width="16" height="16" viewBox="0 0 16 16" fill="#fff" stroke="#fff"><use href="#ico-link"/></svg></span>
    <span><svg width="16" height="16" viewBox="0 0 16 16" fill="var(--glyph)" stroke="var(--glyph)"><use href="#ico-mail"/></svg></span>
    <span><svg width="16" height="16" viewBox="0 0 16 16" fill="var(--glyph)" stroke="var(--glyph)"><use href="#ico-star"/></svg></span>
  </div>
</article>
<article class="card" style="left:801px">
  <div class="portrait" role="img" aria-label="Portrait photo of Tobin Ashcroft" style="background:linear-gradient(180deg,#f2f2f2 0%,#d9a88e 45%,#5a3a3a 100%)"></div>
  <h3 class="member-name">TOBIN ASHCROFT</h3>
  <p class="member-role">Lead Developer</p>
  <p class="member-phone">+1 (555) 0148273</p>
  <p class="member-mail">✉ tobin@coinlantern.example</p>
  <div class="socials">
    <span><svg width="16" height="16" viewBox="0 0 16 16" fill="var(--glyph)" stroke="var(--glyph)"><use href="#ico-share"/></svg></span>
    <span><svg width="16" height="16" viewBox="0 0 16 16" fill="var(--glyph)" stroke="var(--glyph)"><use href="#ico-chat"/></svg></span>
    <span><svg width="16" height="16" viewBox="0 0 16 16" fill="var(--glyph)" stroke="var(--glyph)"><use href="#ico-globe"/></svg></span>
    <span><svg width="16" height="16" viewBox="0 0 16 16" fill="var(--glyph)" stroke="var(--glyph)"><use href="#ico-link"/></svg></span>
    <span><svg width="16" height="16" viewBox="0 0 16 16" fill="var(--glyph)" stroke="var(--glyph)"><use href="#ico-mail"/></svg></span>
    <span><svg width="16" height="16" viewBox="0 0 16 16" fill="var(--glyph)" stroke="var(--glyph)"><use href="#ico-star"/></svg></span>
  </div>
</article>
<div class="to-top" style="left:1110px;top:2459px"><svg width="12" height="8" viewBox="0 0 12 8"><polyline points="1,7 6,2 11,7" fill="none" stroke="#fff" stroke-width="1.6"/></svg></div>

<section class="abs info" role="img" aria-label="Dark band with faint world map"></section>
<div class="info-item" style="left:74px"><div class="info-icon"><svg width="18" height="18" viewBox="0 0 18 18"><circle cx="9" cy="9" r="7" fill="none" stroke="#fff" stroke-width="1.8"/><circle cx="9" cy="9" r="2.6" fill="#fff"/></svg></div><p class="info-label">ADDRESS</p></div>
<div class="info-item" style="left:345px"><div class="info-icon"><svg width="18" height="18" viewBox="0 0 18 18"><path d="M4 1l3 4-2 2c1 2 3 4 5 5l2-2 4 3-2 3C8 16 2 10 1 4z" fill="#fff"/></svg></div><p class="info-label">PHONES</p></div>
<div class="info-item" style="left:615px"><div class="info-icon"><svg width="18" height="14" viewBox="0 0 18 14"><rect x="1" y="1" width="16" height="12" fill="none" stroke="#fff" stroke-width="1.8"/><polyline points="1,1 9,8 17,1" fill="none" stroke="#fff" stroke-width="1.8"/></svg></div><p class="info-label">CONTACTS</p></div>
<div class="info-item" style="left:884px"><div class="info-icon"><svg width="18" height="18" viewBox="0 0 18 18"><circle cx="9" cy="9" r="7.5" fill="none" stroke="#fff" stroke-width="1.8"/><polyline points="9,4 9,9 12,11" fill="none" stroke="#fff" stroke-width="1.8"/></svg></div><p class="info-label">WORKING HOURS</p>
  <p class="hours">Monday-Friday: 9:00 – 18:00<br>Saturday: 11:00 – 17:00<br>Sunday: Closed</p></div>

<footer class="abs footer"></footer>
<div class="foot-brand"><div class="ring"></div><p class="name">CoinLantern</p></div>
<h4 class="foot-title" style="left:620px">OUR CLIENTS</h4>
<span class="client" style="left:631px;top:2937px"></span>
<span class="client" style="left:711px;top:2937px"></span>
<span class="client" style="left:790px;top:2937px"></span>
<span class="client" style="left:631px;top:3015px"></span>
<span class="client" style="left:711px;top:3015px"></span>
<span class="client" style="left:790px;top:3015px;border-radius:0"></span>
<h4 class="foot-title" style="left:888px">NEWSLETTER</h4>
<p class="news-copy">Subscribe to our newsletter and stay up to date with all events coming straight in your mailbox</p>
<div class="news-input">Your email address<span class="news-go"><svg width="8" height="12" viewBox="0 0 8 12"><polyline points="1,1 6,6 1,11" fill="none" stroke="#fff" stroke-width="1.8"/></svg></span></div>

<div class="abs bottom"></div>
<div class="bottom-socials">
  <svg width="13" height="13" viewBox="0 0 16 16" fill="#fff" stroke="#fff"><use href="#ico-share"/></svg>
  <svg width="13" height="13" viewBox="0 0 16 16" fill="#fff" stroke="#fff"><use href="#ico-chat"/></svg>
  <svg width="13" height="13" viewBox="0 0 16 16" fill="#fff" stroke="#fff"><use href="#ico-globe"/></svg>
  <svg width="13" height="13" viewBox="0 0 16 16" fill="#fff" stroke="#fff"><use href="#ico-link"/></svg>
  <svg width="13" height="13" viewBox="0 0 16 16" fill="#fff" stroke="#fff"><use href="#ico-star"/></svg>
  <svg width="13" height="13" viewBox="0 0 16 16" fill="#fff" stroke="#fff"><use href="#ico-mail"/></svg>
</div>
<div class="to-top" style="left:1110px;top:3187px"><svg width="12" height="8" viewBox="0 0 12 8"><polyline points="1,7 6,2 11,7" fill="none" stroke="#fff" stroke-width="1.6"/></svg></div>

</body>
</html>
```